Field Trip Flyer

We need a flyer to promote our field trips. I would like the flyer to be bright, eye popping and modern. We offer STEM Field Trips as well for an educational opportunity that connects roller skating and STEM concepts. We offer field trips for 2 or 3 hours and all field trips include skating, skate rental, play zone, arcade games available, concessions available, + much more! Field trips are fun, unique and engaging and can be booked online at brindlewavefun.com. Our business name is Brindlewave Skate Center. The flyer design needs to be front and back.

Target Market(s)

Elementary School Teachers

Requirements
Must have
• Front and Back Design, 5.5 x 8.5,Field Trip Inclusions: Skating, skate rental, play zone, arcade available, concessions available + much more!, STEM Field Trips available, book online at brindlewavefun.com
Nice to have
• engaging key words to describe the field trips
Should not have
• too much words or irrelevant information

```html
<!DOCTYPE html>
<html lang="en">
<head>
<meta charset="utf-8">
<title>Brindlewave Skate Center – Field Trip Flyer</title>
<link rel="stylesheet" href="https://fonts.googleapis.com/css2?family=Poppins:wght@600;700;800&family=Oswald:wght@500&display=swap">
<style>
  :root {
    --royal: #3341b8;
    --royal-deep: #2a35a3;
    --flag-red: #e8173a;
    --burst-red: #e4202a;
    --ink: #1c1c1c;
    --paper: #ffffff;
    --stage: #f1f1f1;
  }
  * { margin: 0; padding: 0; box-sizing: border-box; }
  html, body { width: 1200px; height: 2342px; overflow: hidden; background: var(--stage); }
  .flyer {
    position: absolute; left: 50px; top: 458px;
    width: 718px; height: 930px;
    transform: scale(1.532); transform-origin: top left;
    background: var(--paper); overflow: hidden;
    box-shadow: 0 6px 18px rgba(0,0,0,.25);
    font-family: "Poppins", sans-serif;
  }
  .backdrop { position: absolute; inset: 0; }
  .photo {
    position: absolute; border-radius: 50%;
    border: 5px solid var(--paper);
    box-shadow: 0 2px 8px rgba(0,0,0,.25);
  }
  .photo--hero { left: 272px; top: -10px; width: 500px; height: 500px;
    background: radial-gradient(circle at 45% 60%, #5a7fc4 0%, #8a6a64 45%, #4b3f3e 100%); }
  .photo--group { left: 484px; top: 425px; width: 192px; height: 192px;
    background: linear-gradient(160deg, #7b4fa0 0%, #c7b9b0 50%, #2f9a46 100%); }
  .photo--rink { left: 468px; top: 625px; width: 212px; height: 212px;
    background: linear-gradient(180deg, #e9c84a 0%, #9db6e0 40%, #dfe6f4 100%); }
  .brand {
    position: absolute; left: 46px; top: 96px; width: 150px;
    color: var(--paper); font-weight: 700; font-size: 17px; line-height: 1.2;
    text-align: center;
  }
  .headline {
    position: absolute; left: 70px; top: 238px;
    color: var(--paper); font-weight: 700; font-size: 44px; line-height: 48px;
  }
  .offer-title { position: absolute; left: 50px; top: 462px; font-size: 40px; font-weight: 700; color: var(--ink); }
  .offer-title span { color: var(--flag-red); }
  .duration { position: absolute; left: 48px; top: 516px; font-size: 21px; font-weight: 700; color: var(--ink); display: flex; align-items: center; gap: 8px; }
  .duration span { color: var(--flag-red); }
  .includes {
    position: absolute; left: 40px; top: 555px; width: 266px; height: 60px;
    border: 4px solid var(--royal); border-radius: 30px; background: var(--paper);
    color: var(--flag-red); font-weight: 700; font-size: 22px;
    display: flex; align-items: center; justify-content: center;
  }
  .includes::after {
    content: ""; position: absolute; left: 152px; bottom: -20px;
    width: 22px; height: 22px; background: var(--paper);
    border-right: 4px solid var(--royal); border-bottom: 4px solid var(--royal);
    transform: rotate(45deg);
  }
  .inclusions { position: absolute; left: 48px; top: 648px; list-style: none; }
  .inclusions li { display: flex; align-items: center; gap: 10px; height: 37.5px; font-size: 22px; font-weight: 600; color: var(--ink); }
  .burst { position: absolute; left: 240px; top: 620px; width: 250px; height: 215px; }
  .burst-text {
    position: absolute; left: 240px; top: 672px; width: 250px;
    text-align: center; color: var(--paper); font-weight: 800; font-size: 21px; line-height: 27px;
  }
  .booking {
    position: absolute; left: 50px; top: 850px; width: 618px; height: 42px;
    border-radius: 14px; overflow: hidden; display: flex;
    font-family: "Oswald", sans-serif; font-weight: 500; font-size: 14.5px; color: var(--paper);
    text-transform: uppercase; letter-spacing: .1px;
  }
  .booking-copy { background: var(--royal); flex: 0 0 470px; display: flex; align-items: center; padding-left: 10px; }
  .booking-site { background: var(--flag-red); flex: 1; display: flex; align-items: center; padding-left: 4px; }
</style>
</head>
<body>
<main class="flyer">
  <svg class="backdrop" viewBox="0 0 718 930" aria-hidden="true">
    <path d="M0 0H718V428C610 468 480 420 360 430C220 442 100 432 0 462Z" fill="var(--royal)"/>
    <path d="M0 480C100 448 220 452 360 444C480 436 610 474 718 440" fill="none" stroke="var(--flag-red)" stroke-width="7"/>
    <g fill="var(--paper)">
      <circle cx="62" cy="300" r="86"/><circle cx="152" cy="258" r="76"/><circle cx="252" cy="270" r="80"/>
      <circle cx="312" cy="330" r="66"/><circle cx="252" cy="382" r="66"/><circle cx="150" cy="388" r="62"/>
      <circle cx="60" cy="372" r="66"/>
    </g>
    <g fill="var(--flag-red)">
      <circle cx="62" cy="300" r="80"/><circle cx="152" cy="258" r="70"/><circle cx="252" cy="270" r="74"/>
      <circle cx="312" cy="330" r="60"/><circle cx="252" cy="382" r="60"/><circle cx="150" cy="388" r="56"/>
      <circle cx="60" cy="372" r="60"/><rect x="40" y="270" width="280" height="110"/>
    </g>
    <circle cx="263" cy="50" r="6" fill="#ff5a7a"/>
    <circle cx="268" cy="148" r="9" fill="#ff7a8a"/>
    <circle cx="617" cy="552" r="7" fill="#ff9a3a"/>
    <circle cx="676" cy="640" r="5" fill="#ff5a7a"/>
  </svg>

  <div class="photo photo--hero" role="img" aria-label="Photo of smiling schoolchildren at the skate center snack counter"></div>
  <div class="photo photo--group" role="img" aria-label="Photo of kids sitting together on the play zone floor"></div>
  <div class="photo photo--rink" role="img" aria-label="Photo of a girl roller skating on the rink"></div>

  <div class="brand">Brindlewave<br>Skate Center</div>
  <h1 class="headline">We offer<br>STEM<br>Field Trips</h1>

  <h2 class="offer-title">We <span>offer</span></h2>
  <p class="duration">
    <svg width="24" height="24" viewBox="0 0 24 24" aria-hidden="true"><path d="M20 12a8 8 0 1 1-3-6.2" fill="none" stroke="var(--flag-red)" stroke-width="3" stroke-linecap="round"/><path d="M14 3h5v5z" fill="var(--flag-red)"/><path d="M12 8v4l3 2" fill="none" stroke="var(--flag-red)" stroke-width="2.4" stroke-linecap="round"/></svg>
    field trips for&nbsp;<span>2 or 3 hours</span>
  </p>
  <p class="includes">All field trips include</p>

  <ul class="inclusions">
    <li><svg width="20" height="20" viewBox="0 0 20 20" aria-hidden="true"><circle cx="10" cy="10" r="10" fill="var(--royal)"/><path d="M5.5 10.5l3 3 6-6.5" fill="none" stroke="#fff" stroke-width="2.4" stroke-linecap="round" stroke-linejoin="round"/></svg>skating</li>
    <li><svg width="20" height="20" viewBox="0 0 20 20" aria-hidden="true"><circle cx="10" cy="10" r="10" fill="var(--royal)"/><path d="M5.5 10.5l3 3 6-6.5" fill="none" stroke="#fff" stroke-width="2.4" stroke-linecap="round" stroke-linejoin="round"/></svg>skate rental</li>
    <li><svg width="20" height="20" viewBox="0 0 20 20" aria-hidden="true"><circle cx="10" cy="10" r="10" fill="var(--royal)"/><path d="M5.5 10.5l3 3 6-6.5" fill="none" stroke="#fff" stroke-width="2.4" stroke-linecap="round" stroke-linejoin="round"/></svg>play zone</li>
    <li><svg width="20" height="20" viewBox="0 0 20 20" aria-hidden="true"><circle cx="10" cy="10" r="10" fill="var(--royal)"/><path d="M5.5 10.5l3 3 6-6.5" fill="none" stroke="#fff" stroke-width="2.4" stroke-linecap="round" stroke-linejoin="round"/></svg>arcade</li>
    <li><svg width="20" height="20" viewBox="0 0 20 20" aria-hidden="true"><circle cx="10" cy="10" r="10" fill="var(--royal)"/><path d="M5.5 10.5l3 3 6-6.5" fill="none" stroke="#fff" stroke-width="2.4" stroke-linecap="round" stroke-linejoin="round"/></svg>games available</li>
  </ul>

  <svg class="burst" viewBox="-125 -125 250 250" preserveAspectRatio="none" aria-hidden="true">
    <polygon fill="var(--burst-red)" points="125,0 103,20.5 115.5,47.9 87.3,58.4 88.4,88.4 58.4,87.3 47.9,115.5 20.5,103 0,125 -20.5,103 -47.9,115.5 -58.4,87.3 -88.4,88.4 -87.3,58.4 -115.5,47.9 -103,20.5 -125,0 -103,-20.5 -115.5,-47.9 -87.3,-58.4 -88.4,-88.4 -58.4,-87.3 -47.9,-115.5 -20.5,-103 0,-125 20.5,-103 47.9,-115.5 58.4,-87.3 88.4,-88.4 87.3,-58.4 115.5,-47.9 103,-20.5"/>
  </svg>
  <p class="burst-text">concessions<br>available,<br>+<br>much more!</p>

  <p class="booking">
    <span class="booking-copy">Field trips are fun, unique and engaging and can be booked online</span>
    <span class="booking-site">at brindlewavefun.com</span>
  </p>
</main>
</body>
</html>
```